Cell phone case packaging

Looking to have our own cell phone case packaging design. The pakaging will hold smart phone case. Looking for something that would fit an 8 x 10 size. The packaging should match the colors of this website www.velandrotel.example.

In the back i would like to have the definition of the work Joy.

Joie: Sentiment de plaisir, de bonheur intense, caractérisé par sa plénitude et sa durée limitée, et éprouvé par quelqu'un dont une aspiration, un désir est satisfait ou en voie de l'être

Joy: the emotion of great delight or happiness caused by something exceptionally good or satisfying; keen pleasure; elation

I prefer a clam shell design. I have attach examples of packaging designs i like

Industry/Entity Type

Wireless Communication

Font styles to use
Sans Serif

Colors
0255a3
33b8a4
fece3e
f04a50

Requirements
Must have
• 1. Ability to feel the texture of the case
• 2. must be all in french
• 3. very colorful
• 3. must be able to place on hook

```html
<!DOCTYPE html>
<html lang="fr">
<head>
<meta charset="utf-8">
<title>Joie — emballage étui</title>
<link rel="stylesheet" href="https://fonts.googleapis.com/css2?family=Questrial&display=swap">
<style>
  :root {
    --lime: #cbd423;
    --amber: #f1b22e;
    --orange: #f28a35;
    --coral: #ea4a45;
    --red: #ec1d2b;
    --white: #ffffff;
    --ornament-dark: #2a2a2a;
    --ornament-mid: #8f8f8f;
    --ornament-light: #e4e4e4;
    --leaf-glow: rgba(255, 196, 90, 0.55);
    --leaf-soft: rgba(255, 170, 110, 0.28);
  }
  html, body {
    margin: 0;
    padding: 0;
    width: 960px;
    height: 1200px;
    overflow: hidden;
    background: var(--white);
  }
  .back-panel {
    position: relative;
    width: 960px;
    height: 1200px;
    overflow: hidden;
    background: linear-gradient(180deg,
      var(--lime) 0%,
      var(--lime) 16%,
      var(--amber) 36%,
      var(--orange) 50%,
      var(--coral) 63%,
      var(--red) 78%,
      var(--red) 100%);
  }
  .leaf-motif {
    position: absolute;
    left: 170px;
    top: 235px;
    width: 720px;
    height: 880px;
    border-radius: 46% 46% 38% 38% / 40% 40% 44% 44%;
    background:
      radial-gradient(ellipse 60% 48% at 50% 34%, var(--leaf-glow) 0%, rgba(255, 190, 90, 0.3) 55%, rgba(255, 190, 90, 0) 100%),
      radial-gradient(ellipse 70% 55% at 50% 70%, var(--leaf-soft) 0%, rgba(255, 160, 140, 0) 100%);
  }
  .ornament-border {
    position: absolute;
    top: 0;
    height: 1200px;
  }
  .ornament-border--left {
    left: 0;
    width: 100px;
    background: linear-gradient(90deg, var(--ornament-mid) 0%, var(--ornament-light) 45%, var(--ornament-mid) 80%, var(--ornament-dark) 100%);
    border-radius: 0 48px 48px 0;
  }
  .ornament-border--right {
    right: 0;
    width: 90px;
    background: linear-gradient(270deg, var(--ornament-mid) 0%, var(--ornament-light) 45%, var(--ornament-mid) 80%, var(--ornament-dark) 100%);
    border-radius: 48px 0 0 48px;
  }
  .definition {
    position: absolute;
    left: 108px;
    width: 760px;
    top: 942px;
    text-align: center;
    color: var(--white);
    font-family: "Questrial", sans-serif;
  }
  .definition__word {
    margin: 0;
    font-size: 56px;
    font-weight: 400;
    line-height: 66px;
  }
  .definition__text {
    margin: -2px 0 0;
    font-size: 25.5px;
    line-height: 36px;
    white-space: nowrap;
  }
</style>
</head>
<body>
  <main class="back-panel">
    <div class="leaf-motif" role="img" aria-label="Feuille d'érable translucide en filigrane"></div>
    <div class="ornament-border ornament-border--left" role="img" aria-label="Bordure de fleurs stylisées noires et grises"></div>
    <div class="ornament-border ornament-border--right" role="img" aria-label="Bordure de fleurs stylisées noires et grises"></div>
    <section class="definition">
      <h1 class="definition__word">Joie</h1>
      <p class="definition__text">Sentiment de plaisir, de bonheur intense, caractérisé<br>par sa plénitude et sa durée limitée, et éprouvé par<br>quelqu'un dont une aspiration, un désir est satisfait ou<br>en voie de l'être</p>
    </section>
  </main>
</body>
</html>
```